New Phone Case requires logo and packaging

We need a nice and sleek logo designed along with packaging for our Premium Phone Case brand

Our Brand Name is Vaxel
Please note this has nothing to do with a Rhino so don't put a Rhino in the logo
I've also attached a file called VAXEL Logo Inspiration, which shows something along the lines of the type of text we want to use. Please note i have photoshopped that image together from another logo we had, and i liked the text, but its for you to see what direction we want to go in. Also note i have shown different variations in that image file, use your imagination with it and show us a nice and clean logo.

We would like the Brand in upper caps such as VAXEL
The brand is for Premium Phone Cases. The first thing that should come to someones mind when looking at the branding is High Quality, Premium and Modern.

The look must be high end and modern

The design must portray high quality and premium!

Also i will say "Less is More". Don't cramp many things on the packaging and logo. We just want a nice, clean cut high quality logo and packaging

I have attached images of an example packaging from a few competitors. One is a standard open from top packaging, while another is a slide out packaging. Our packaging dimensions should be the same which are Packaging dimensions
Length = 18cm
Height = 1.5cm
Depth = 9.5cm

Also note the example packaging has a transparent front section to show which case is inside, this is optional if you want to have it. If not you can cover it all up.

Font styles to use
Other font styles liked:
• Any nice font but just not the standard everyday stuff like Arial, San Serif etc as i want it to be differentiated. A Font that shows Serious Quality and one that stands out would be awesome!

Colors

Designer to choose colors to be used in the design.

Requirements
Must have
• Must be a nice and clean design
• Packaging dimensions
• Length = 18cm
• Height = 1.5cm
• Depth = 9.5cm

```html
<!DOCTYPE html>
<html lang="en">
<head>
<meta charset="utf-8">
<title>Vaxel – Logo and Packaging</title>
<link rel="stylesheet" href="https://fonts.googleapis.com/css2?family=Montserrat:wght@500;700&family=Source+Sans+3:wght@300;400&display=swap">
<style>
  :root {
    --card: #f0e0ca;
    --green: #72bf44;
    --ink: #000000;
    --label: #8c8c8c;
    --paper: #ffffff;
  }
  html, body { margin: 0; padding: 0; overflow: hidden; background: var(--paper); }
  .canvas { position: relative; width: 1200px; height: 900px; overflow: hidden; background: var(--paper); }

  .wordmark {
    position: absolute; left: 28px; top: 12px; margin: 0;
    font-family: "Montserrat", sans-serif; font-weight: 700;
    font-size: 172px; line-height: 1; letter-spacing: 4px; color: var(--ink);
  }

  .label {
    position: absolute; margin: 0;
    font-family: "Source Sans 3", sans-serif; font-weight: 300;
    font-size: 20px; line-height: 1; color: var(--label); white-space: nowrap;
  }
  .label--material { left: 696px; top: 148px; }
  .label--front { left: 286px; width: 354px; top: 178px; text-align: center; }
  .label--spine-a { left: 648px; width: 76px; top: 178px; text-align: center; }
  .label--back { left: 733px; width: 353px; top: 178px; text-align: center; }
  .label--spine-b { left: 1094px; width: 76px; top: 178px; text-align: center; }

  .panel { position: absolute; top: 204px; height: 668px; }
  .panel--front { left: 286px; width: 354px; background: var(--card); }
  .panel--back { left: 733px; width: 353px; background: var(--card); }
  .spine { width: 56px; background: var(--green); }
  .spine--a { left: 658px; }
  .spine--b { left: 1104px; }

  .front-art { position: absolute; left: 0; top: 0; }
  .window-label { left: 160px; top: 86px; }

  .front-name {
    position: absolute; left: 60px; top: 264px; margin: 0;
    font-family: "Montserrat", sans-serif; font-weight: 700;
    font-size: 39px; line-height: 1; letter-spacing: 2px; color: var(--green);
  }

  .features { position: absolute; left: 0; top: 378px; width: 354px; margin: 0; padding: 0; list-style: none; }
  .dots {
    height: 8px; margin-left: 27px; width: 305px;
    background: radial-gradient(circle, var(--ink) 1.8px, transparent 2.3px) 0 0 / 25.4px 8px repeat-x;
  }
  .feature {
    height: 68px; display: flex; align-items: center; justify-content: center;
    font-family: "Montserrat", sans-serif; font-weight: 500;
    font-size: 14px; letter-spacing: 2px; color: var(--green);
  }

  .spine-name {
    position: absolute; left: 28px; top: 334px; margin: 0;
    transform: translate(-50%, -50%) rotate(-90deg);
    font-family: "Montserrat", sans-serif; font-weight: 700;
    font-size: 40px; line-height: 1; letter-spacing: 2px; color: var(--paper); white-space: nowrap;
  }

  .back-note {
    position: absolute; left: 0; width: 353px; top: 306px; margin: 0; text-align: center;
    font-family: "Source Sans 3", sans-serif; font-weight: 300;
    font-size: 20px; line-height: 25px; color: var(--label);
  }
</style>
</head>
<body>
<main class="canvas">
  <h1 class="wordmark">VAXEL</h1>

  <p class="label label--material">Packaging made from natural, unbleached card stock</p>
  <p class="label label--front">[Front of Package]</p>
  <p class="label label--spine-a">[Spine]</p>
  <p class="label label--back">[Back of Package]</p>
  <p class="label label--spine-b">[Spine]</p>

  <section class="panel panel--front" aria-label="Front of package">
    <svg class="front-art" width="354" height="668" viewBox="0 0 354 668">
      <polygon class="front-window" points="44,38 316,38 316,308" fill="#ffffff" stroke="#ffffff" stroke-width="8" stroke-linejoin="round"/>
      <polygon class="front-flag" points="46,104 46,307 248,307" fill="#000000" stroke="#000000" stroke-width="6" stroke-linejoin="round"/>
    </svg>
    <p class="label window-label">[Front Window]</p>
    <p class="front-name">VAXEL</p>
    <ul class="features">
      <li class="dots" aria-hidden="true"></li>
      <li class="feature">FULL PROTECTION</li>
      <li class="dots" aria-hidden="true"></li>
      <li class="feature">PREFECT FIT</li>
      <li class="dots" aria-hidden="true"></li>
      <li class="feature">MADE FROM GREEN MATERIALS</li>
      <li class="dots" aria-hidden="true"></li>
    </ul>
  </section>

  <section class="panel spine spine--a" aria-label="Spine">
    <p class="spine-name">VAXEL</p>
  </section>

  <section class="panel panel--back" aria-label="Back of package">
    <p class="back-note">[Technical Specifications<br>&amp; Bar Code]</p>
  </section>

  <section class="panel spine spine--b" aria-label="Spine">
    <p class="spine-name">VAXEL</p>
  </section>
</main>
</body>
</html>
```